Kinward Harbor Center
Stationary and Business Cards
Kinward Harbor Center -
Creative Brief
Bright & Fun-filled
Marisol Thackery
48 Alder Lane Larkfield, NJ 07931
marisol.thackery@alderlanehub.org
www.alderlanehub.org

```html
<!DOCTYPE html>
<html lang="en">
<head>
<meta charset="utf-8">
<title>Kinward Harbor Center – Stationery</title>
<link href="https://fonts.googleapis.com/css2?family=Open+Sans:wght@400;600;700&display=swap" rel="stylesheet">
<style>
  :root {
    --backdrop: #a9abae;
    --paper: #ffffff;
    --blue-deep: #1d4f98;
    --blue-mid: #2f6cc0;
    --blue-light: #5b93db;
    --accent-grey: #8e9196;
    --accent-orange: #e58a2b;
    --ink: #4a4d52;
    --ink-soft: #7b7e83;
  }
  * { margin: 0; padding: 0; box-sizing: border-box; }
  html, body { width: 1200px; height: 626px; overflow: hidden; }
  body {
    background: var(--backdrop);
    font-family: "Open Sans", Arial, sans-serif;
    color: var(--ink);
    position: relative;
  }
  .piece { position: absolute; background: var(--paper); overflow: hidden; box-shadow: 0 2px 6px rgba(0,0,0,.18); }
  .piece svg.shape { position: absolute; inset: 0; width: 100%; height: 100%; }

  .brand { position: absolute; display: flex; flex-direction: column; align-items: center; text-align: center; white-space: nowrap; }
  .brand-mark { width: 14px; height: 14px; border-radius: 50%; background: var(--blue-mid); margin-bottom: 3px; }
  .brand-name { font-weight: 600; font-size: 7px; letter-spacing: .12em; text-transform: uppercase; color: var(--blue-deep); }
  .brand-tag { font-size: 4.5px; color: var(--ink-soft); letter-spacing: .05em; margin-top: 1px; }

  .contact { position: absolute; font-size: 5px; line-height: 1.55; color: var(--ink); text-align: left; white-space: nowrap; }
  .web { position: absolute; font-size: 5.5px; color: var(--accent-orange); white-space: nowrap; }

  /* Business card */
  .business-card { left: 29px; top: 305px; width: 163px; height: 122px; border-radius: 6px; }
  .business-card .holder { position: absolute; left: 10px; top: 6px; font-size: 5.5px; font-weight: 600; color: #fff; }
  .business-card .holder small { display: block; font-weight: 400; font-size: 4.5px; opacity: .85; }
  .business-card .brand { left: 58px; top: 40px; }
  .business-card .brand-name { font-size: 5.5px; }
  .business-card .brand-tag { font-size: 3.6px; }
  .business-card .web { left: 10px; top: 78px; font-size: 4.5px; color: var(--blue-deep); }
  .business-card .contact { left: 10px; top: 86px; font-size: 4px; }

  /* Letterhead */
  .letterhead { left: 233px; top: 29px; width: 420px; height: 561px; }
  .letterhead .brand { left: 150px; top: 24px; }
  .letterhead .contact { left: 318px; top: 14px; }
  .letterhead .web { left: 318px; top: 535px; }

  /* Envelope back */
  .envelope-back { left: 679px; top: 79px; width: 497px; height: 226px; }

  /* Envelope front */
  .envelope-front { left: 679px; top: 336px; width: 497px; height: 211px; }
  .envelope-front .brand { left: 40px; top: 28px; }
  .envelope-front .brand-name { font-size: 5.5px; }
  .envelope-front .brand-tag { font-size: 3.8px; }
  .envelope-front .contact { left: 312px; top: 26px; }
  .envelope-front .web { left: 400px; top: 178px; font-size: 5px; }
</style>
</head>
<body>

<section class="piece business-card">
  <svg class="shape" viewBox="0 0 163 122" preserveAspectRatio="none">
    <defs>
      <linearGradient id="cardBlue" x1="0" x2="1">
        <stop offset="0" stop-color="var(--blue-deep)"/><stop offset="1" stop-color="var(--blue-light)"/>
      </linearGradient>
    </defs>
    <path d="M0,0 H163 V14 Q110,22 60,20 Q20,19 0,28 Z" fill="url(#cardBlue)"/>
    <path d="M0,30 Q22,21 62,22 Q112,24 163,16" fill="none" stroke="var(--accent-orange)" stroke-width="1.2"/>
    <path d="M0,122 H163 V114 Q100,110 0,118 Z" fill="var(--accent-grey)" opacity=".5"/>
  </svg>
  <p class="holder">Marisol Thackery<small>Executive Director</small></p>
  <div class="brand">
    <span class="brand-mark"></span>
    <span class="brand-name">Kinward Harbor Center</span>
    <span class="brand-tag">Connecting Families, Building Community</span>
  </div>
  <p class="web">www.alderlanehub.org</p>
  <p class="contact">P: 555 014 2210<br>marisol.thackery@alderlanehub.org<br>48 Alder Lane Larkfield, NJ 07931</p>
</section>

<section class="piece letterhead">
  <svg class="shape" viewBox="0 0 420 561" preserveAspectRatio="none">
    <defs>
      <linearGradient id="sheetBlue" x1="0" x2="0" y1="0" y2="1">
        <stop offset="0" stop-color="var(--blue-deep)"/><stop offset=".5" stop-color="var(--blue-light)"/><stop offset="1" stop-color="var(--blue-deep)"/>
      </linearGradient>
    </defs>
    <rect width="420" height="561" fill="url(#sheetBlue)"/>
    <path d="M86,0 Q-34,280 66,561" fill="none" stroke="var(--accent-grey)" stroke-width="9"/>
    <path d="M86,0 Q-30,280 70,561 H420 V0 Z" fill="var(--paper)"/>
  </svg>
  <div class="brand">
    <span class="brand-mark"></span>
    <span class="brand-name">Kinward Harbor Center</span>
    <span class="brand-tag">Connecting Families, Building Community</span>
  </div>
  <p class="contact">P: 555 014 2210<br>F: 555 014 2211<br>marisol.thackery@alderlanehub.org<br>48 Alder Lane Larkfield, NJ 07931</p>
  <p class="web">www.alderlanehub.org</p>
</section>

<section class="piece envelope-back">
  <svg class="shape" viewBox="0 0 497 226" preserveAspectRatio="none">
    <defs>
      <radialGradient id="flapBlue" cx=".5" cy=".25" r=".7">
        <stop offset="0" stop-color="var(--blue-light)"/><stop offset="1" stop-color="var(--blue-deep)"/>
      </radialGradient>
    </defs>
    <path d="M0,0 H497 V150 Q497,178 469,178 H28 Q0,178 0,150 Z" fill="url(#flapBlue)"/>
  </svg>
</section>

<section class="piece envelope-front">
  <svg class="shape" viewBox="0 0 497 211" preserveAspectRatio="none">
    <defs>
      <linearGradient id="envBlue" x1="0" x2="0" y1="0" y2="1">
        <stop offset="0" stop-color="var(--blue-mid)"/><stop offset="1" stop-color="var(--blue-deep)"/>
      </linearGradient>
    </defs>
    <rect width="60" height="211" fill="url(#envBlue)"/>
    <path d="M46,0 Q6,105 36,211" fill="none" stroke="var(--accent-grey)" stroke-width="6"/>
    <path d="M46,0 Q10,105 40,211 H497 V0 Z" fill="var(--paper)"/>
  </svg>
  <div class="brand">
    <span class="brand-mark"></span>
    <span class="brand-name">Kinward Harbor Center</span>
    <span class="brand-tag">Connecting Families, Building Community</span>
  </div>
  <p class="contact">P: 555 014 2210<br>F: 555 014 2211<br>marisol.thackery@alderlanehub.org<br>48 Alder Lane Larkfield, NJ 07931</p>
  <p class="web">www.alderlanehub.org</p>
</section>

</body>
</html>
```